Business Card Design Project

We are an agricultural business based in Brisbane.
We design, manage and operate regional saleyards. Our logo is green/silver in colour and details of our business can be found on our website www.tovrak.com.au

Just wanting a corporate design for some business cards and include name, position, contact details.

Thanks

```html
<!DOCTYPE html>
<html lang="en">
<head>
<meta charset="utf-8">
<title>Tovrak – Business Card</title>
<link rel="stylesheet" href="https://fonts.googleapis.com/css2?family=Josefin+Sans:wght@400;600;700&display=swap">
<style>
  :root {
    --page: #ffffff;
    --card-back: #f1f1f1;
    --brand-green: #00883f;
    --divider-green: #1fa653;
    --ink: #111111;
    --paper: #ffffff;
  }
  * { margin: 0; padding: 0; box-sizing: border-box; }
  html, body {
    width: 1200px;
    height: 1000px;
    overflow: hidden;
    background: var(--page);
    font-family: "Josefin Sans", sans-serif;
  }
  .canvas { position: relative; width: 1200px; height: 1000px; }

  .card { position: absolute; width: 692px; height: 422px; overflow: hidden; }

  /* Reverse side */
  .card-reverse { left: 100px; top: 100px; background: var(--card-back); }
  .card-reverse .wordmark {
    position: absolute; left: 0; right: 0; top: 176px;
    text-align: center; font-size: 64px;
  }

  /* Front side */
  .card-front { left: 408px; top: 477px; background: var(--paper); }
  .card-front .band { position: absolute; inset: 0; }
  .card-front .wordmark {
    position: absolute; left: 0; right: 0; top: 52px;
    text-align: center; font-size: 42px;
  }

  .wordmark {
    font-weight: 700; color: var(--ink);
    letter-spacing: 0.06em; text-transform: uppercase; line-height: 1;
  }

  .contact-block {
    position: absolute; left: 0; right: 0; top: 204px;
    text-align: center;
  }
  .person-name {
    color: var(--paper); font-weight: 600; font-size: 27px;
    letter-spacing: 0.1em; text-transform: uppercase; line-height: 1;
  }
  .person-role {
    color: var(--paper); font-size: 20px; letter-spacing: 0.05em;
    margin-top: 12px; line-height: 1;
  }
  .divider { display: block; margin: 16px auto 0; }
  .contact-line {
    color: var(--ink); font-size: 16px; letter-spacing: 0.03em; line-height: 1;
  }
  .contact-line.phones { margin-top: 22px; }
  .contact-line.email { margin-top: 13px; }
  .sep { margin: 0 6px; }
</style>
</head>
<body>
<main class="canvas">
  <section class="card card-reverse" aria-label="Card reverse">
    <div class="wordmark">Tovrak</div>
  </section>

  <section class="card card-front" aria-label="Card front">
    <svg class="band" width="692" height="422" viewBox="0 0 692 422" aria-hidden="true">
      <polygon points="0,108 347,151 692,108 692,422 0,422" fill="var(--brand-green)"/>
    </svg>
    <div class="wordmark">Tovrak</div>
    <div class="contact-block">
      <div class="person-name">Mark Ellison</div>
      <div class="person-role">Marketing Director</div>
      <svg class="divider" width="110" height="8" viewBox="0 0 110 8" aria-hidden="true">
        <polygon points="0,0 110,0 55,8" fill="var(--divider-green)"/>
      </svg>
      <div class="contact-line phones">p: 555.014.2368<span class="sep">|</span>m: 555.014.2368</div>
      <div class="contact-line email">e: mellison@tovrak.com.au</div>
    </div>
  </section>
</main>
</body>
</html>
```